Online medical reviews website needs banner advert!

We need banner advert templates for our website, www.traineepanel.net. These should meet the technical requirements of our partner (uploaded).

Our groundbreaking website allows doctors in training to rate and review their training.

The adverts should use the same modern design language and colour scheme as our website. They should use the text 'Help a junior doctor make a big decision - rate your training!'.

Vector assets should be supplied, allowing us to use alternative text in future.
Updates

Industry/Entity Type

Healthcare

Font styles to use
Other font styles liked:
• Karla

Colors
3277b5
0555a3
ffffff

Requirements
Must have
• Similar design to our website. Should be elegant & modern. Must allow future text to be easily inserted.
Should not have
• Unrelated design.

```html
<!DOCTYPE html>
<html lang="en">
<head>
<meta charset="utf-8">
<title>Trainee Panel – Banner Adverts</title>
<link href="https://fonts.googleapis.com/css2?family=Fredoka:wght@400;500;600&display=swap" rel="stylesheet">
<style>
  :root {
    --brand-blue: #3277b5;
    --brand-deep: #0555a3;
    --bright-blue: #2e8be0;
    --white: #ffffff;
    --ink: #1c1c1c;
    --black: #121212;
    --stage-light: #ffffff;
    --stage-dark: #a6a6a6;
    --map-tint: #e9edf2;
  }
  * { box-sizing: border-box; margin: 0; padding: 0; }
  html, body { width: 1200px; height: 1200px; overflow: hidden; }
  body {
    background: linear-gradient(to bottom, var(--stage-dark) 0%, var(--stage-light) 40%, var(--stage-light) 52%, var(--stage-dark) 100%);
    font-family: "Fredoka", sans-serif;
    position: relative;
  }
  .banner {
    position: absolute;
    left: 110px;
    width: 982px;
    height: 91px;
    box-shadow: 0 2px 6px rgba(0,0,0,0.35);
    overflow: hidden;
  }
  .banner--dark { top: 493px; background: var(--black); }
  .banner--light { top: 671px; background: var(--white); }
  .banner__shapes { position: absolute; inset: 0; }
  .headline {
    position: absolute;
    color: var(--white);
    text-align: center;
    line-height: 1;
  }
  .headline__lead { display: block; font-weight: 600; font-size: 22px; letter-spacing: -0.3px; }
  .headline__cta { display: block; font-weight: 600; font-size: 26px; margin-top: 7px; }
  .banner--dark .headline { left: 0; width: 496px; top: 19px; }
  .url-button {
    position: absolute;
    top: 31px;
    height: 40px;
    width: 216px;
    border-radius: 4px;
    display: flex;
    align-items: center;
    justify-content: center;
    font-size: 16px;
    font-weight: 400;
  }
  .url-button--white {
    left: 728px;
    background: linear-gradient(#ffffff, #e4e4e4);
    color: var(--ink);
    box-shadow: 0 1px 3px rgba(0,0,0,0.5);
  }
  .illustration {
    position: absolute;
    left: 0; top: 0;
    width: 242px; height: 91px;
    background: radial-gradient(ellipse at 50% 55%, #3f7fc8 0%, #8fb3de 35%, #ffffff 70%);
  }
  .banner__panel {
    position: absolute;
    left: 242px; top: 0;
    width: 445px; height: 91px;
    background: var(--brand-blue);
  }
  .banner--light .headline { left: 242px; width: 445px; top: 22px; }
  .banner--light .headline__lead { font-size: 21px; }
  .banner--light .headline__cta { margin-top: 6px; }
  .map-area {
    position: absolute;
    left: 687px; top: 0;
    width: 295px; height: 91px;
    background: radial-gradient(ellipse at 45% 40%, var(--map-tint) 0%, #f6f8fa 55%, #ffffff 80%);
  }
  .url-button--blue {
    left: 733px;
    top: 31px;
    background: var(--brand-deep);
    color: var(--white);
    font-size: 16px;
  }
</style>
</head>
<body>

<section class="banner banner--dark" aria-label="Banner advert, dark variant">
  <svg class="banner__shapes" width="982" height="91" viewBox="0 0 982 91">
    <defs>
      <linearGradient id="blueField" x1="0" y1="0" x2="0" y2="1">
        <stop offset="0" stop-color="#2e8be0"/>
        <stop offset="1" stop-color="#1f6fc4"/>
      </linearGradient>
      <linearGradient id="photoTone" x1="0" y1="0" x2="1" y2="1">
        <stop offset="0" stop-color="#f3f3f3"/>
        <stop offset="0.55" stop-color="#d9dde2"/>
        <stop offset="1" stop-color="#9cc3ea"/>
      </linearGradient>
    </defs>
    <rect width="982" height="91" fill="#121212"/>
    <polygon points="0,0 500,0 478,91 0,91" fill="url(#blueField)"/>
    <polygon points="503,0 507,0 485,91 481,91" fill="#ffffff"/>
    <g role="img" aria-label="Photo of hands typing on a laptop beside printed charts">
      <polygon points="510,0 700,0 678,91 488,91" fill="url(#photoTone)"/>
    </g>
    <polygon points="700,0 708,0 686,91 678,91" fill="#2e8be0"/>
    <polygon points="982,0 982,91 952,91" fill="#2e8be0"/>
  </svg>
  <h2 class="headline">
    <span class="headline__lead">Help a junior doctor make a big decision</span>
    <span class="headline__cta">rate your training</span>
  </h2>
  <div class="url-button url-button--white">www.traineepanel.net</div>
</section>

<section class="banner banner--light" aria-label="Banner advert, light variant">
  <div class="illustration" role="img" aria-label="Illustration of large blue WWW letters with small business figures walking around them"></div>
  <div class="banner__panel"></div>
  <h2 class="headline">
    <span class="headline__lead">Help a junior doctor make a big decision</span>
    <span class="headline__cta">rate your training</span>
  </h2>
  <div class="map-area" role="img" aria-label="Faint grey world map background"></div>
  <div class="url-button url-button--blue">www.traineepanel.net</div>
</section>

</body>
</html>
```